Gladly Call Corwin Consulting needs a new and exciting customer online experience (Webpage)

Gladly Call Corwin is a new and exciting IT and Telecoms business. We aim to help business with all of its technology needs.

The business has only been around less than 12 months and a page was developed to give some online presence, but now its time for a refresh. The page is very bland and boring. It needs some creative zing to give it that pop whilst maintaining a professional appeal.

Our current page can be found at www.gladlycallcorwin.example.au

I have included below some of our current marketing. I've included our business cards and some of messages on hold we are running.

Target Market(s)

Small to medium business, small enterprise

Industry/Entity Type

Business

Number of Pages Required

5+ page

Font styles to use
Sans Serif

Requirements
Must have
• The page must have some colour. IT and Telecoms can be mundane and boring. We want people to be engaged in their IT and Telecoms. We want them to feel as passionate about their IT and Telecoms as we do.
• It must have the following pages: Home, About Us, Services We provide, Contact Us and our Blog Page.
• The contact us should have an option to complete an online form which is delivered to our enquiries email.
• We would also like to have our social media links for Chatterbook, WorkWeave and Quorra plus. The pages must also contain a link to our privacy policy located near the bottom of the page

```html
<!DOCTYPE html>
<html lang="en">
<head>
<meta charset="utf-8">
<title>Gladly Call Corwin Consulting</title>
<link rel="stylesheet" href="https://fonts.googleapis.com/css2?family=Open+Sans:wght@400;600&family=Varela+Round&display=swap">
<style>
  :root {
    --navy: #3a3470;
    --navy-panel: rgba(55, 47, 110, 0.92);
    --blue: #0aa6d8;
    --green: #8cb832;
    --red: #d8143a;
    --text: #222;
    --muted: #777;
    --rule: #e3e3e3;
    --page: #fdfdfd;
    --footer: #f2f2f2;
  }
  * { margin: 0; padding: 0; box-sizing: border-box; }
  html, body { width: 1116px; height: 1200px; overflow: hidden; }
  body { position: relative; background: var(--page); font-family: "Open Sans", sans-serif; color: var(--text); }
  a { color: inherit; text-decoration: none; }

  .site-header { position: absolute; left: 0; top: 0; width: 1116px; height: 108px; background: #fff; }
  .brand { position: absolute; left: 134px; top: 28px; display: flex; align-items: center; gap: 12px; font-family: "Varela Round", sans-serif; color: var(--navy); }
  .brand-dot { width: 46px; height: 46px; border-radius: 50%; background: var(--blue); }
  .brand-name { font-size: 27px; line-height: 1.05; }
  .brand-name small { display: block; font-size: 19px; padding-left: 66px; }
  .phone { position: absolute; right: 139px; top: 21px; display: flex; align-items: center; gap: 4px; color: var(--blue); font-family: "Varela Round", sans-serif; font-size: 18px; }
  .main-nav { position: absolute; top: 63px; left: 553px; display: flex; gap: 36px; font-family: "Varela Round", sans-serif; font-size: 15.5px; color: var(--navy); }

  .hero { position: absolute; left: 0; top: 108px; width: 1116px; height: 437px; background: linear-gradient(90deg, #9fb3c4 0%, #5a6b7a 35%, #2d3a3c 55%, #56603a 75%, #4a6585 100%); }
  .hero-caption { position: absolute; left: 131px; top: 163px; width: 363px; height: 140px; background: var(--navy-panel); color: #fff; padding: 28px 0 0 28px; }
  .hero-caption h1 { font-family: "Varela Round", sans-serif; font-weight: 400; font-size: 31px; line-height: 1.1; }
  .hero-caption p { font-family: "Varela Round", sans-serif; font-size: 14px; line-height: 1.3; margin-top: 8px; }
  .hero-arrow { position: absolute; top: 173px; width: 52px; height: 52px; border-radius: 50%; background: rgba(255,255,255,0.85); display: flex; align-items: center; justify-content: center; }
  .hero-arrow.prev { left: 50px; }
  .hero-arrow.next { left: 1010px; }
  .hero-dots { position: absolute; top: 413px; left: 539px; display: flex; gap: 4px; }
  .hero-dots span { width: 11px; height: 11px; border-radius: 50%; background: #fff; }

  .features { position: absolute; top: 573px; left: 151px; width: 818px; height: 250px; }
  .feature { position: absolute; top: 0; width: 256px; height: 247px; }
  .feature-photo { width: 256px; height: 108px; }
  .feature h2 { font-family: "Varela Round", sans-serif; font-weight: 400; font-size: 18px; margin: 10px 0 6px 4px; }
  .feature p { font-size: 10.3px; line-height: 1.62; color: var(--muted); margin-left: 4px; width: 230px; }
  .feature .btn { position: absolute; top: 202px; left: 3px; width: 87px; height: 26px; border-radius: 2px; color: #fff; font-size: 10px; font-weight: 600; display: flex; align-items: center; justify-content: center; }
  .feature .bar { position: absolute; top: 244px; left: 0; width: 256px; height: 3px; }
  .feature.what { left: 0; } .feature.what h2 { color: var(--blue); }
  .feature.what .btn, .feature.what .bar { background: var(--blue); }
  .feature.what .feature-photo { background: linear-gradient(135deg, #2b2d30, #6d7368 60%, #b0a27a); }
  .feature.services { left: 282px; } .feature.services h2 { color: var(--green); margin-top: 14px; }
  .feature.services .btn, .feature.services .bar { background: var(--green); }
  .feature.services .feature-photo { background: linear-gradient(135deg, #d7dde3, #8da2b8 55%, #3f4b56); }
  .feature.contact { left: 562px; } .feature.contact h2 { color: var(--red); margin-top: 13px; }
  .feature.contact .btn, .feature.contact .bar { background: var(--red); }
  .feature.contact .feature-photo { background: linear-gradient(135deg, #c9b39a, #e8e2da 50%, #9fb0c0); }
  .divider { position: absolute; top: 0; width: 1px; height: 250px; background: var(--rule); }

  .intro { position: absolute; top: 874px; left: 160px; width: 520px; }
  .intro h2 { font-family: "Varela Round", sans-serif; font-weight: 400; font-size: 26px; line-height: 1.28; color: #333; }
  .intro .lead { font-size: 12.5px; margin: 12px 0 6px; }
  .intro p { font-size: 10.4px; line-height: 1.6; color: var(--muted); margin-bottom: 5px; }

  .recent-blog { position: absolute; top: 874px; left: 710px; width: 270px; }
  .recent-blog h2 { font-family: "Varela Round", sans-serif; font-weight: 400; font-size: 24px; color: var(--navy); margin-bottom: 10px; }
  .post { margin-bottom: 14px; }
  .post h3 { font-family: "Varela Round", sans-serif; font-weight: 400; font-size: 13px; color: var(--blue); margin-bottom: 5px; }
  .post p { font-size: 10.4px; line-height: 1.6; color: var(--muted); }

  .site-footer { position: absolute; top: 1108px; left: 0; width: 1116px; height: 92px; background: var(--footer); }
  .footer-nav { position: absolute; left: 152px; top: 22px; font-family: "Varela Round", sans-serif; font-size: 12.5px; color: #333; }
  .footer-nav span { margin: 0 7px; }
  .legal { position: absolute; left: 152px; top: 47px; font-size: 9.6px; color: var(--muted); }
  .social { position: absolute; left: 891px; top: 24px; display: flex; gap: 8px; }
  .social a { width: 20px; height: 20px; border-radius: 2px; }
  .social .chatterbook { background: #3b5998; }
  .social .chirpline { background: #3fb7e8; }
  .social .workweave { background: #1c75b4; }
</style>
</head>
<body>
  <header class="site-header">
    <a class="brand" href="#">
      <span class="brand-dot"></span>
      <span class="brand-name">Gladly Call Corwin<small>Consulting</small></span>
    </a>
    <div class="phone">
      <svg width="22" height="22" viewBox="0 0 22 22" aria-hidden="true"><circle cx="11" cy="11" r="10" fill="none" stroke="#bbb" stroke-width="1.5"/><path d="M8 6c-1 1-1 3 1 6s4 4 5 3l1-1-2-2-1 1c-1 0-3-2-3-3l1-1-2-2z" fill="#bbb"/></svg>
      (08) 7410 3926
    </div>
    <nav class="main-nav">
      <a href="#">Home</a><a href="#">About Us</a><a href="#">Services</a><a href="#">Blog</a><a href="#">Contact Us</a>
    </nav>
  </header>

  <section class="hero" role="img" aria-label="Photo of two IT consultants working on a laptop beside a network server rack">
    <div class="hero-caption">
      <h1>IT Business Consulting</h1>
      <p>Lorem ipsum dolor sit amet consectetuer adipiscing elit Nam cursus Morbi</p>
    </div>
    <a class="hero-arrow prev" href="#" aria-label="Previous slide"><svg width="16" height="26" viewBox="0 0 16 26"><path d="M13 2 3 13l10 11" fill="none" stroke="#3a3470" stroke-width="2.5"/></svg></a>
    <a class="hero-arrow next" href="#" aria-label="Next slide"><svg width="16" height="26" viewBox="0 0 16 26"><path d="M3 2l10 11L3 24" fill="none" stroke="#3a3470" stroke-width="2.5"/></svg></a>
    <div class="hero-dots"><span></span><span></span><span></span><span></span></div>
  </section>

  <section class="features">
    <article class="feature what">
      <div class="feature-photo" role="img" aria-label="Photo of two businessmen in a data centre"></div>
      <h2>What We Do</h2>
      <p>Curabitur iaculis tempus eros Curabitur vel mi sit amet magna malesuada ultrices Ut nisi erat fermentum vel congue id euismod</p>
      <a class="btn" href="#">READ MORE</a>
      <div class="bar"></div>
    </article>
    <div class="divider" style="left:268px"></div>
    <article class="feature services">
      <div class="feature-photo" role="img" aria-label="Photo of two technicians talking beside a server rack"></div>
      <h2>Services Provides</h2>
      <p>Curabitur iaculis tempus eros Curabitur vel mi sit amet magna malesuada ultrices Ut nisi erat fermentum vel congue id euismod</p>
      <a class="btn" href="#">READ MORE</a>
      <div class="bar"></div>
    </article>
    <div class="divider" style="left:549px"></div>
    <article class="feature contact">
      <div class="feature-photo" role="img" aria-label="Photo of support staff wearing headsets"></div>
      <h2>How to Contact Us</h2>
      <p>Curabitur iaculis tempus eros Curabitur vel mi sit amet magna malesuada ultrices Ut nisi erat fermentum vel congue id euismod</p>
      <a class="btn" href="#">READ MORE</a>
      <div class="bar"></div>
    </article>
  </section>

  <section class="intro">
    <h2>Making IT and Telecommunications Simple for business</h2>
    <p class="lead">Mauris vel lacus vitae felis vestibulum volutpat Etiam est nunc venenatis in tristique</p>
    <p>Vivamus porttitor g purus nisi eleifend libero a tempus libero lectus feugiat felis Morbi diam mauris viverra in gravida eu mattis in ante Morbi eget arcu Morbi porta libero id ullamcorper</p>
    <p>Nonummy nibh ligula pulvinar metus eget consectetuer augue nisi quis lacus Ut ac mi quis lacus mollis aliquam Curabitur iaculis tempus eros Curabitur vel mi sit amet magna malesuada ultrices</p>
  </section>

  <aside class="recent-blog">
    <h2>Recent Blog</h2>
    <div class="post">
      <h3>Aorbi diam mauris viverra</h3>
      <p>in gravida eu mattis in ante Morbi eget arcu Morbi</p>
    </div>
    <div class="post">
      <h3>Mauris vel lacus vitae felis</h3>
      <p>Etiam est nunc venenatis in tristique eu imperdiet ac nisl Cum sociis natoque penatibus et</p>
    </div>
  </aside>

  <footer class="site-footer">
    <nav class="footer-nav">
      <a href="#">Home</a><span>|</span><a href="#">About Us</a><span>|</span><a href="#">Services</a><span>|</span><a href="#">Blog</a><span>|</span><a href="#">Contact Us</a>
    </nav>
    <p class="legal">© 2014 Company Name &nbsp;All right reserved &nbsp;Term of Use</p>
    <div class="social">
      <a class="chatterbook" href="#" aria-label="Chatterbook"></a>
      <a class="chirpline" href="#" aria-label="Chirpline"></a>
      <a class="workweave" href="#" aria-label="WorkWeave"></a>
    </div>
  </footer>
</body>
</html>
```